KOR Design

Looking for the website design of an small business,
The company is newly established. The Company Trades with Steel from Asiam Europe to Australia and New Zealand.

In the main Page, we would like to have a video showing the process of how steel is made(or the iron melt, pipe rolled, etc)

We would like to show pictures of the Products we trade and an table with some information about the specifications and Product.

About the company,
Industry is Iron and Steel
The company source and supply various steel and metal products within our international network also manage all aspects of the supply process from point of manufacture to point of delivery. the goal is to create value within the supply chain by building strong supplier, customers and service providers, funding of both customers and suppliers, experienced risk management, efficient document handling.
Main products: LSAW pipe, ERW Pipe, Flat rolled Products (such is Steel Coil, Aluminium Zinc Coil, Floor Plate, Plate, etc), Reinforcing bar

Number of Pages Required

5+ page

Font styles to use
Sans Serif

Requirements
Must have
• Video in the home page showing

```html
<!DOCTYPE html>
<html lang="en">
<head>
<meta charset="utf-8">
<title>KOR Design – Steel Trading</title>
<link href="https://fonts.googleapis.com/css2?family=Poppins:wght@500;600;700&family=Roboto:wght@400;500;700&display=swap" rel="stylesheet">
<style>
:root{
  --orange:#f05a14;
  --orange-deep:#e14e0c;
  --navy:#0c2350;
  --navy-dark:#081a3d;
  --ink:#1f1f1f;
  --text:#333;
  --muted:#555;
  --light:#f3f3f5;
  --white:#fff;
  --steel:#8c939c;
}
*{margin:0;padding:0;box-sizing:border-box}
html,body{width:1200px;height:4200px;overflow:hidden}
body{position:relative;font-family:"Roboto",Arial,sans-serif;color:var(--text);background:var(--white)}
.abs{position:absolute}
h1,h2,h3{font-weight:700}
.btn{position:absolute;background:var(--orange);color:var(--white);font-family:"Roboto",Arial,sans-serif;font-weight:700;border-radius:24px;display:flex;align-items:center;justify-content:center;letter-spacing:.3px}

/* nav */
.nav{position:absolute;left:0;top:0;width:1200px;height:101px;background:var(--white)}
.brand{position:absolute;left:100px;top:30px;display:flex;align-items:center;gap:10px;font-family:"Poppins",sans-serif;font-weight:700;font-size:30px;color:var(--navy)}
.brand i{width:16px;height:16px;background:var(--orange);display:block}
.menu{position:absolute;right:118px;top:42px;display:flex;gap:37px;font-size:17px;color:#222}
.menu .active{color:var(--orange)}

/* hero */
.hero{position:absolute;left:0;top:101px;width:1200px;height:558px;background:linear-gradient(135deg,#3a3f45 0%,#8a8e92 35%,#5a5f66 60%,#2d3034 100%)}
.hero-box{position:absolute;left:73px;top:160px;width:781px;height:252px;background:rgba(20,22,26,.45)}
.hero h1{position:absolute;left:108px;top:190px;font-family:"Poppins",sans-serif;font-size:72px;color:var(--white);line-height:1}
.hero p{position:absolute;left:108px;top:286px;width:700px;font-size:24px;line-height:40px;color:var(--white)}
.hero .btn{left:108px;top:381px;width:153px;height:46px;font-size:18px}
.dots{position:absolute;display:flex;gap:12px}
.dots span{width:7px;height:7px;border-radius:50%;background:var(--white)}
.dots .on{background:var(--orange)}

/* about */
.about{position:absolute;left:0;top:659px;width:1200px;height:563px;background:var(--white)}
.about-fade{position:absolute;left:0;top:420px;width:1200px;height:143px;background:linear-gradient(180deg,#eef0f3,#f7f8fa)}
.about h2{position:absolute;left:111px;top:112px;font-family:"Poppins",sans-serif;font-weight:600;font-size:40px;color:var(--ink)}
.about p{position:absolute;left:111px;top:178px;width:525px;font-size:16.5px;line-height:36px;color:#333;text-align:justify}
.about .btn{left:108px;top:418px;width:144px;height:48px;font-size:18px}
.frame-orange{position:absolute;left:866px;top:107px;width:241px;height:227px;background:var(--orange);clip-path:polygon(0 0,100% 0,100% 100%,88% 93%,88% 9%,0 9%)}
.frame-navy{position:absolute;left:703px;top:234px;width:239px;height:232px;background:var(--navy);clip-path:polygon(0 10%,10% 0,10% 92%,80% 92%,100% 100%,0 100%)}
.video{position:absolute;left:727px;top:132px;width:355px;height:309px;background:linear-gradient(135deg,#6f7780,#c9ced3 40%,#9aa1a8 70%,#5e656c);border:5px solid var(--white)}
.play{position:absolute;left:867px;top:248px}

/* products */
.products{position:absolute;left:0;top:1222px;width:1200px;height:571px;background:var(--navy)}
.products-photo{position:absolute;left:0;top:5px;width:456px;height:566px;background:linear-gradient(135deg,#4a5058,#b9bec4 45%,#7c838b 70%,#3d424a);clip-path:polygon(0 0,85% 0,100% 48%,82% 100%,0 100%)}
.products-edge{position:absolute;left:0;top:0}
.products h2{position:absolute;left:491px;top:82px;font-family:"Poppins",sans-serif;font-size:33px;color:var(--white);font-weight:600}
.spec{position:absolute;left:492px;top:155px;width:618px;border:3px solid #6d7893;border-collapse:collapse;font-size:16px}
.spec th{background:var(--orange);color:var(--white);font-weight:400;height:57px;text-align:left;padding-left:28px;border-right:2px solid #d9d9d9}
.spec td{background:#b3b8c3;color:#1e2a44;height:52px;padding-left:28px;border-top:3px solid #6d7893;border-right:2px solid #6d7893;vertical-align:middle}
.spec td:not(:first-child){vertical-align:top;padding-top:10px;padding-left:10px}

/* why */
.why{position:absolute;left:0;top:1793px;width:1200px;height:644px;background:var(--white)}
.why-band{position:absolute;left:5px;top:0;width:1195px;height:143px;background:var(--light)}
.why h2{position:absolute;left:0;top:94px;width:1200px;text-align:center;font-family:"Poppins",sans-serif;font-size:36px;color:#2a2a2a;font-weight:600}
.why .lead{position:absolute;left:160px;top:165px;width:880px;text-align:center;font-size:17px;line-height:34px;color:#222}
.feature{position:absolute;top:285px;width:230px;text-align:center}
.feature svg{display:block;margin:0 auto}
.feature p{margin-top:34px;font-size:20px;line-height:33px;color:#222}

/* testimonials */
.testi{position:absolute;left:0;top:2440px;width:1200px;height:543px;background:linear-gradient(135deg,#f06418,#e5520e 60%,#ef6a22)}
.testi h2{position:absolute;left:0;top:64px;width:1176px;text-align:center;font-family:"Poppins",sans-serif;font-size:38px;color:var(--white);font-weight:600}
.avatar{position:absolute;left:522px;top:152px;width:90px;height:90px;border-radius:50%;background:linear-gradient(180deg,#d9d2ca,#9b8f85);border:4px solid var(--white)}
.quote{position:absolute;font-family:"Poppins",sans-serif;font-size:140px;line-height:1;color:rgba(255,255,255,.55);font-weight:700}
.testi .body{position:absolute;left:220px;top:265px;width:700px;text-align:center;font-size:15.5px;line-height:30px;color:var(--white)}
.testi .who{position:absolute;left:0;top:410px;width:1180px;text-align:center;font-size:15.5px;line-height:30px;color:var(--white);font-style:italic}

/* blog */
.blog h2{position:absolute;left:0;top:3080px;width:1200px;text-align:center;font-family:"Poppins",sans-serif;font-size:39px;color:#2a2a2a;font-weight:600}
.card{position:absolute;top:3183px;width:326px;height:465px;border:1px solid #ddd;background:#fafafa}
.card .img{position:absolute;left:9px;top:9px;width:306px;height:187px}
.card .date{position:absolute;left:16px;top:219px;font-size:15px;color:var(--orange);font-weight:500}
.card h3{position:absolute;left:16px;top:250px;width:300px;font-size:15.5px;line-height:29px;color:#222}
.card p{position:absolute;left:16px;top:316px;width:300px;font-size:13px;line-height:26px;color:#444}
.card .btn{left:16px;top:402px;width:140px;height:44px;font-size:17px}
.side-dots{position:absolute;left:1137px;top:3350px;display:flex;flex-direction:column;gap:11px}
.side-dots span{width:8px;height:8px;border-radius:50%;background:#222}

/* footer */
.footer{position:absolute;left:0;top:3744px;width:1200px;height:456px;background:var(--navy)}
.foot-brand{position:absolute;left:98px;top:130px;display:flex;align-items:center;gap:14px;font-family:"Poppins",sans-serif;font-weight:700;font-size:56px;color:var(--white)}
.foot-brand i{width:22px;height:22px;border-radius:50%;background:var(--orange);display:block}
.footer h4{position:absolute;top:62px;font-family:"Roboto",sans-serif;font-weight:700;font-size:20px;color:var(--white);letter-spacing:.3px}
.contact{position:absolute;left:375px;display:flex;align-items:flex-start;gap:18px;color:var(--white);font-size:16px;line-height:26px}
.contact svg{flex:none}
.links{position:absolute;left:712px;top:122px;list-style:none;color:var(--white);font-size:17px}
.links li{height:40px;display:flex;align-items:center;gap:10px}
.social{position:absolute;left:940px;top:115px;list-style:none;color:var(--white);font-size:17px}
.social li{height:52px;display:flex;align-items:center;gap:18px}
.social i{width:34px;height:34px;border-radius:50%;border:2px solid var(--white);display:flex;align-items:center;justify-content:center}
.social i b{width:12px;height:12px;border-radius:50%;background:var(--white);display:block}
.copy{position:absolute;left:0;top:404px;width:1178px;text-align:center;font-size:16px;color:var(--white)}
</style>
</head>
<body>

<header class="nav">
  <div class="brand"><i></i>KOR</div>
  <nav class="menu">
    <span class="active">Home</span><span>About us</span><span>services</span><span>Our products</span><span>Specifications</span><span>Contact us</span>
  </nav>
</header>

<section class="hero">
  <div class="abs" role="img" aria-label="Stacked steel pipes photograph" style="inset:0"></div>
  <div class="hero-box"></div>
  <h1>KOR</h1>
  <p>Neque porro quisquam est qui dolorem ipsum quia dolor sit amet, consectetur, adipisci velit.</p>
  <div class="btn">GET STARTED</div>
  <div class="dots" style="left:580px;top:524px"><span></span><span class="on"></span><span></span></div>
</section>

<section class="about">
  <div class="about-fade"></div>
  <h2>ABOUT US</h2>
  <p>The company source and supply various steel and metal products within our internationalnetwork also manage all aspects of the supply process from point of manufacture to point of delivery. the goal is to create value within the supply chain by building strong supplier, customers and service providers, funding of both customers and suppliers, experienced riskmanagement, efficient document handling.</p>
  <div class="btn">READ MORE</div>
  <div class="frame-orange"></div>
  <div class="frame-navy"></div>
  <div class="video" role="img" aria-label="Video still of galvanised steel coils in a warehouse"></div>
  <svg class="play" width="76" height="76" viewBox="0 0 76 76"><circle cx="38" cy="38" r="38" fill="#0c2350"/><path d="M30 24 L54 38 L30 52 Z" fill="#fff"/></svg>
</section>

<section class="products">
  <div class="products-photo" role="img" aria-label="Rolled steel coils in a factory"></div>
  <svg class="products-edge" width="460" height="571" viewBox="0 0 460 571"><polyline points="381,0 456,272 381,571" fill="none" stroke="#fff" stroke-width="5"/></svg>
  <h2>OUR PRODUCTS SPECIFICATIONS</h2>
  <table class="spec">
    <tr><th style="width:178px">Product Name</th><th style="width:150px">Weight</th><th style="width:133px">Value</th><th>Unite</th></tr>
    <tr><td>LSAW Pipe</td><td>120</td><td>pa/m'3</td><td>7850</td></tr>
    <tr><td>ERW Pipe</td><td>85.4</td><td>Pa</td><td>2,07E+11</td></tr>
    <tr><td>Flat Rolled</td><td>35</td><td>Pa</td><td>0.3</td></tr>
    <tr><td>Pipe, Flat rolle</td><td>45.5</td><td>Pa</td><td>7.9615E+10</td></tr>
    <tr><td>Steel Coil</td><td>75.8</td><td>Pa</td><td>2.5E+08</td></tr>
  </table>
</section>

<section class="why">
  <div class="why-band"></div>
  <h2>WHY CHOOSE KOR</h2>
  <p class="lead">Sed ut perspiciatis unde omnis iste natus error sit voluptatem accusantium doloremque laudantium, totam rem aperiam, eaque ipsa quae ab illo inventore veritatis et quasi architecton.</p>

  <div class="feature" style="left:79px">
    <svg width="184" height="184" viewBox="0 0 184 184"><path d="M2 92 A90 90 0 0 0 182 92 L168 92 A76 76 0 0 1 16 92 Z" fill="#f05a14"/><circle cx="92" cy="92" r="76" fill="#fff" stroke="#ddd" stroke-width="2"/><circle cx="92" cy="92" r="62" fill="#0c2350"/><circle cx="86" cy="98" r="24" fill="none" stroke="#fff" stroke-width="3"/><path d="M86 84 V98 H98" fill="none" stroke="#fff" stroke-width="3"/><circle cx="112" cy="74" r="14" fill="#0c2350" stroke="#fff" stroke-width="3"/><text x="112" y="80" fill="#fff" font-size="16" text-anchor="middle" font-family="Roboto,sans-serif">24</text></svg>
    <p>Neque porro quisquam est qui dolorem.</p>
  </div>
  <div class="feature" style="left:328px">
    <svg width="184" height="184" viewBox="0 0 184 184"><path d="M2 92 A90 90 0 0 1 182 92 L168 92 A76 76 0 0 0 16 92 Z" fill="#f05a14"/><circle cx="92" cy="92" r="76" fill="#fff" stroke="#ddd" stroke-width="2"/><circle cx="92" cy="92" r="62" fill="#0c2350"/><path d="M62 76 H84 L110 108 H88 Z M84 76 H106 L122 96 V108 H110" fill="none" stroke="#fff" stroke-width="3"/></svg>
    <p>Neque porro quisquam est qui dolorem.</p>
  </div>
  <div class="feature" style="left:589px">
    <svg width="184" height="184" viewBox="0 0 184 184"><path d="M2 92 A90 90 0 0 0 182 92 L168 92 A76 76 0 0 1 16 92 Z" fill="#f05a14"/><circle cx="92" cy="92" r="76" fill="#fff" stroke="#ddd" stroke-width="2"/><circle cx="92" cy="92" r="62" fill="#0c2350"/><rect x="72" y="62" width="40" height="60" rx="4" fill="none" stroke="#fff" stroke-width="3"/><circle cx="92" cy="92" r="12" fill="none" stroke="#fff" stroke-width="2.5"/><text x="92" y="98" fill="#fff" font-size="16" text-anchor="middle" font-family="Roboto,sans-serif">$</text><path d="M62 84 H72 M62 100 H72 M112 84 H124 M112 100 H124" stroke="#fff" stroke-width="2.5"/></svg>
    <p>Neque porro quisquam est qui dolorem.</p>
  </div>
  <div class="feature" style="left:863px">
    <svg width="184" height="184" viewBox="0 0 184 184"><path d="M2 92 A90 90 0 0 1 182 92 L168 92 A76 76 0 0 0 16 92 Z" fill="#f05a14"/><circle cx="92" cy="92" r="76" fill="#fff" stroke="#ddd" stroke-width="2"/><circle cx="92" cy="92" r="62" fill="#0c2350"/><path d="M62 106 H110 L116 70 H124" fill="none" stroke="#fff" stroke-width="3"/><rect x="68" y="90" width="16" height="14" fill="none" stroke="#fff" stroke-width="2.5"/><rect x="88" y="78" width="18" height="26" fill="none" stroke="#fff" stroke-width="2.5"/><circle cx="74" cy="116" r="5" fill="none" stroke="#fff" stroke-width="2.5"/><circle cx="102" cy="116" r="5" fill="none" stroke="#fff" stroke-width="2.5"/></svg>
    <p>Neque porro quisquam est qui dolorem.</p>
  </div>
</section>

<section class="testi">
  <div class="abs" role="img" aria-label="Orange toned steel pipe ends background" style="inset:0"></div>
  <h2>TESTIMONIALS</h2>
  <div class="avatar" role="img" aria-label="Client portrait"></div>
  <div class="quote" style="left:146px;top:165px">&ldquo;</div>
  <div class="quote" style="left:944px;top:300px">&rdquo;</div>
  <p class="body">At vero eos et accusamus et iusto odio dignissimos ducimus qui blanditiis praesentium voluptatum deleniti atque corrupti quos dolores et quas molestias excepturi sint occaecati cupiditate non provident, similique sunt in culpa qui officia deserunt mollitia animi, id est laborum et dolorum fuga. Et harum quidem rerum facilis est et expedita distinctio.</p>
  <p class="who">Morgan<br>At vero eos et accusamus</p>
  <div class="dots" style="left:566px;top:500px;gap:27px"><span style="width:9px;height:9px"></span><span style="width:9px;height:9px"></span></div>
</section>

<section class="blog">
  <h2>LATEST BLOG</h2>
  <article class="card" style="left:81px">
    <div class="img" role="img" aria-label="Steel floor plate with tread pattern" style="background:linear-gradient(135deg,#2c3138,#9aa3ad 45%,#4b525a 75%,#1e2227)"></div>
    <div class="date">01 Oct, 2020</div>
    <h3>Neque porro quisquam est qui dolorem ipsum quia dolor sit.</h3>
    <p>Lorem Ipsum is simply dummy text of the printing and typesetting industry. Lorem Ipsum has been the industry's standard dummy</p>
    <div class="btn">READ MORE</div>
  </article>
  <article class="card" style="left:440px">
    <div class="img" role="img" aria-label="Stacked pipes with blue end caps" style="background:linear-gradient(135deg,#1d3b6e,#3f74c4 40%,#7e8791 70%,#2a3344)"></div>
    <div class="date">01 Oct, 2020</div>
    <h3>Neque porro quisquam est qui dolorem ipsum quia dolor sit.</h3>
    <p>Lorem Ipsum is simply dummy text of the printing and typesetting industry. Lorem Ipsum has been the industry's standard dummy</p>
    <div class="btn">READ MORE</div>
  </article>
  <article class="card" style="left:794px">
    <div class="img" role="img" aria-label="Galvanised steel coils" style="background:linear-gradient(135deg,#6d747c,#d3d7db 45%,#8f969e 70%,#50565d)"></div>
    <div class="date">01 Oct, 2020</div>
    <h3>Neque porro quisquam est qui dolorem ipsum quia dolor sit.</h3>
    <p>Lorem Ipsum is simply dummy text of the printing and typesetting industry. Lorem Ipsum has been the industry's standard dummy</p>
    <div class="btn">READ MORE</div>
  </article>
  <div class="side-dots"><span></span><span></span><span></span></div>
</section>

<footer class="footer">
  <div class="foot-brand"><i></i>KOR</div>
  <h4 style="left:375px">CONTACTS</h4>
  <div class="contact" style="top:118px;align-items:center">
    <svg width="40" height="40" viewBox="0 0 40 40"><circle cx="20" cy="20" r="18.5" fill="none" stroke="#fff" stroke-width="2"/><path d="M14 12 L18 12 L19 17 L16.5 18.5 C17.5 21 19 22.5 21.5 23.5 L23 21 L28 22 L28 26 C20 27 13 20 14 12 Z" fill="#fff"/></svg>555-014-2290
  </div>
  <div class="contact" style="top:180px;align-items:center">
    <svg width="40" height="40" viewBox="0 0 40 40"><circle cx="20" cy="20" r="18.5" fill="none" stroke="#fff" stroke-width="2"/><rect x="12" y="14" width="16" height="12" rx="1" fill="#fff"/><path d="M12 14 L20 21 L28 14" fill="none" stroke="#0c2350" stroke-width="1.6"/></svg>info@KOR.com
  </div>
  <div class="contact" style="top:240px">
    <svg width="40" height="40" viewBox="0 0 40 40"><circle cx="20" cy="20" r="18.5" fill="none" stroke="#fff" stroke-width="2"/><path d="M20 30 C15 23 13 20 13 17 A7 7 0 0 1 27 17 C27 20 25 23 20 30 Z" fill="#fff"/><circle cx="20" cy="17" r="2.6" fill="#0c2350"/></svg>
    <span style="padding-top:4px;font-size:15px">Sed ut perspiciatis unde omnis<br>iste natus error sit voluptatem,</span>
  </div>
  <h4 style="left:704px">QUICK LINKS</h4>
  <ul class="links">
    <li>&#187; Home</li><li>&#187; About us</li><li>&#187; services</li><li>&#187; Our products</li><li>&#187; Specifications</li><li>&#187; Contact us</li>
  </ul>
  <h4 style="left:940px">FOLLOW US</h4>
  <ul class="social">
    <li><i><b></b></i>Friendbook</li>
    <li><i><b></b></i>Chirper</li>
    <li><i><b></b></i>ViewTube</li>
  </ul>
  <p class="copy">Copyrights 2020. All rights reserved</p>
</footer>

</body>
</html>
```